Vellurotrick

I need a poster design for an upcoming show. I'm a magician I have a picture I'd like to use as the basic format but I need verbiage and other border ideas and fonts

Target Market(s)

All ages

Industry/Entity Type

Entertainment Industry

Font styles to use
Sans Serif

Requirements
Must have
• On top of the poster I need VELLURO and at the bottom the word Magician. The names have to pop! I'm open to font ideas. A Border, all text regarding show time date ect.
• Brackenford convention center
• Aug. 21st
• 8:30 pm
• 555-318-4076
• Brackenfordvisit.example
• Also I'd like to have the tv appearances I've made on the poster off to the side wt in some kind of bubble/star/screen and inside that have the tv shows I've been on logos such as NATION OF MARVELS FINALIST, The Morwen show, QVB, ZPN, this is basically a lore for people to come to the show.
Nice to have
• A border, filigree
Should not have
• Top hat, rabbit

```html
<!DOCTYPE html>
<html lang="en">
<head>
<meta charset="utf-8">
<title>Velluro – Magician</title>
<link rel="stylesheet" href="https://fonts.googleapis.com/css2?family=Lobster&family=Oswald:wght@400;500;600&family=Rye&display=swap">
<style>
  :root {
    --peach: #f2dccb;
    --charcoal: #3d3b3a;
    --charcoal-light: #5a5755;
    --red: #c23b2c;
    --blue: #3f79c4;
    --cream: #fbf3e8;
    --orange: #f7941d;
    --orange-dark: #e8621f;
    --orange-deep: #d2481c;
    --paper: #f3d7a4;
    --photo-deep: #141e3c;
    --photo-mid: #2d4e8c;
    --photo-light: #7fa6d4;
  }
  html, body {
    margin: 0;
    padding: 0;
    width: 848px;
    height: 1200px;
    overflow: hidden;
    background: var(--peach);
  }
  .poster {
    display: block;
    width: 848px;
    height: 1200px;
  }
  .headline {
    font-family: "Rye", serif;
    font-size: 190px;
  }
  .headline-shadow { fill: var(--blue); }
  .headline-face { fill: var(--red); }
  .script {
    font-family: "Lobster", cursive;
    font-size: 190px;
  }
  .script-shadow { fill: var(--blue); }
  .script-outline { fill: var(--cream); }
  .script-face { fill: var(--red); }
  .banner-text {
    font-family: "Oswald", sans-serif;
    font-weight: 500;
    fill: #ffffff;
  }
  .tag-phone {
    font-family: "Oswald", sans-serif;
    font-weight: 500;
    font-size: 34px;
    fill: #ffffff;
  }
  .tag-web {
    font-family: "Oswald", sans-serif;
    font-weight: 500;
    font-size: 15px;
    fill: #ffffff;
  }
  .note-text {
    font-family: "Oswald", sans-serif;
    fill: var(--red);
  }
</style>
</head>
<body>
<svg class="poster" viewBox="0 0 848 1200" xmlns="http://www.w3.org/2000/svg">
  <defs>
    <linearGradient id="charcoal-fade" x1="0" y1="0" x2="1" y2="1">
      <stop offset="0" stop-color="var(--charcoal)"/>
      <stop offset="0.5" stop-color="var(--charcoal-light)"/>
      <stop offset="1" stop-color="var(--charcoal)"/>
    </linearGradient>
    <linearGradient id="stage-tones" x1="0" y1="0" x2="0.6" y2="1">
      <stop offset="0" stop-color="var(--photo-deep)"/>
      <stop offset="0.45" stop-color="var(--photo-mid)"/>
      <stop offset="0.75" stop-color="var(--photo-light)"/>
      <stop offset="1" stop-color="var(--photo-mid)"/>
    </linearGradient>
    <linearGradient id="page-curl" x1="0" y1="0" x2="1" y2="1">
      <stop offset="0" stop-color="#ffffff"/>
      <stop offset="1" stop-color="#e9d2bd"/>
    </linearGradient>
  </defs>

  <!-- border: charcoal corners around the heart-shaped field -->
  <rect class="border-field" width="848" height="1200" fill="url(#charcoal-fade)"/>
  <path class="heart-field" fill="var(--peach)"
        d="M0 150 C 70 70, 250 40, 372 0 L 478 0 C 600 40, 780 70, 848 150
           L 848 900 Q 640 1020, 424 1165 Q 208 1020, 0 900 Z"/>

  <!-- headline -->
  <g class="headline">
    <text class="headline-shadow" x="78" y="318" textLength="705" lengthAdjust="spacingAndGlyphs">VELLURO</text>
    <text class="headline-face" x="70" y="312" textLength="705" lengthAdjust="spacingAndGlyphs">VELLURO</text>
  </g>

  <!-- show photograph -->
  <g class="show-photo">
    <path d="M150 356 L 668 356 L 722 410 L 722 1092 L 150 1092 Z" fill="var(--cream)" opacity="0.8"/>
    <rect x="162" y="366" width="550" height="716" fill="url(#stage-tones)"
          role="img" aria-label="Stage photo of the magician with an assistant, tilting a clear cube on stage"/>
    <path d="M612 356 L 668 356 L 722 410 L 722 470 Q 700 420, 660 430 Q 640 390, 612 356 Z" fill="url(#page-curl)"/>
  </g>

  <!-- venue banner -->
  <g class="venue-banner">
    <path d="M752 472 L 842 472 L 830 522 L 842 575 L 752 575 Z" fill="var(--orange-dark)"/>
    <path d="M770 478 L 786 478 L 774 572 L 760 572 Z" fill="var(--orange-deep)"/>
    <rect x="400" y="472" width="356" height="103" fill="var(--orange)"/>
    <text class="banner-text" x="406" y="518" font-size="27" textLength="346" lengthAdjust="spacingAndGlyphs">BRACKENFORD CONVENTION CENTER</text>
    <text class="banner-text" x="452" y="562" font-size="27">Aug. 21st</text>
    <text class="banner-text" x="632" y="562" font-size="27">8:30 PM</text>
  </g>

  <!-- contact tag -->
  <g class="contact-tag">
    <path d="M38 612 L 238 612 Q 238 630, 250 632 L 250 686 Q 238 688, 238 706 L 38 706 Q 38 688, 26 686 L 26 632 Q 38 630, 38 612 Z" fill="var(--orange)"/>
    <path d="M170 694 L 248 706 L 238 712 L 160 700 Z" fill="var(--orange-dark)"/>
    <text class="tag-phone" x="138" y="660" text-anchor="middle">555-318-4076</text>
    <text class="tag-web" x="138" y="688" text-anchor="middle">brackenfordvisit.example</text>
  </g>

  <!-- Magician script -->
  <g class="script" transform="rotate(-8 424 900)">
    <text class="script-shadow" x="34" y="972" textLength="780" lengthAdjust="spacingAndGlyphs">Magician</text>
    <text class="script-outline" x="30" y="968" textLength="780" lengthAdjust="spacingAndGlyphs">Magician</text>
    <text class="script-face" x="24" y="962" textLength="780" lengthAdjust="spacingAndGlyphs">Magician</text>
  </g>

  <!-- TV appearances note -->
  <g class="tv-note">
    <path d="M318 1026 L 572 1026 L 572 1192 L 318 1192
             L 326 1176 L 316 1160 L 326 1144 L 316 1128 L 326 1112
             L 316 1096 L 326 1080 L 316 1064 L 326 1048 L 316 1036 Z" fill="var(--paper)"/>
    <text class="note-text" x="362" y="1056" font-size="20" textLength="154" lengthAdjust="spacingAndGlyphs">You have seen him</text>
    <text class="note-text" x="474" y="1084" font-size="32" font-weight="500" textLength="40" lengthAdjust="spacingAndGlyphs">on</text>
    <text class="note-text" x="520" y="1084" font-size="44" font-weight="500" textLength="48" lengthAdjust="spacingAndGlyphs">TV:</text>
    <text class="note-text" x="358" y="1104" font-size="14" font-weight="600" textLength="208" lengthAdjust="spacingAndGlyphs">NATION OF MARVELS FINALIST</text>
    <text class="note-text" x="516" y="1132" font-size="19">QVB</text>
    <text class="note-text" x="366" y="1138" font-size="21" textLength="136" lengthAdjust="spacingAndGlyphs">The Morwen Show</text>
    <text class="note-text" x="408" y="1186" font-size="34" font-weight="500">ZPN</text>
  </g>
</svg>
</body>
</html>
```